Stationery Design Project

I am looking for stationary design for an automotive collision repair company. This needs to work with my business cards just designed here. I've attached. I need 8.5 x 11 stationary and corissponding envelopes. a post it note pad also. Our companies focus is very high end customer service driven . Our customer base is 35-65 middle to high income. Please include company name, logo, address, phone number, web address. The business card is two greys with green and white writing. I invision a light grey background with a darker grey band on it that contains the logo.

I justĀ 

Why is no one touching this project

Target Market(s)

60%. Women 40% men. Age 35-60

Industry/Entity Type

Automotive

Requirements
Must have
• Tie in with business cards. So it needs grey tones with green and white logo. Name, address, phone and web address. Must have 8.5 x 11 paper and envelopes.
Nice to have
• Post it notes

```html
<!DOCTYPE html>
<html lang="en">
<head>
<meta charset="utf-8">
<title>Panelcraft Stationery</title>
<link href="https://fonts.googleapis.com/css2?family=Arimo:wght@400;700&display=swap" rel="stylesheet">
<style>
  :root {
    --backdrop: #dcdcdc;
    --paper: #ffffff;
    --band: #353133;
    --band-soft: #8c8a8b;
    --brand-green: #8cc63f;
    --text-light: #e6e6e6;
    --text-dark: #333333;
    --shadow: rgba(0, 0, 0, 0.35);
  }
  * { margin: 0; padding: 0; box-sizing: border-box; }
  html, body {
    width: 1200px; height: 900px; overflow: hidden;
    background: var(--backdrop);
    font-family: "Arimo", Arial, sans-serif;
  }
  .sheet {
    position: absolute;
    background: var(--paper);
    box-shadow: 6px 8px 14px var(--shadow);
    overflow: hidden;
  }
  .band { position: absolute; left: 0; width: 100%; display: block; }
  .wordmark {
    position: absolute;
    font-family: "Arimo", Arial, sans-serif;
    font-weight: 700;
    color: var(--brand-green);
    letter-spacing: 0.01em;
    white-space: nowrap;
  }

  /* Letterhead */
  .letterhead { left: 25px; top: 100px; width: 525px; height: 681px; }
  .letterhead .band--top { top: 0; height: 94px; }
  .letterhead .band--bottom { bottom: 0; height: 60px; }
  .letterhead .wordmark { left: 60px; top: 45px; font-size: 22px; }
  .letterhead .contact {
    position: absolute; right: 14px; top: 26px;
    text-align: right; font-size: 9px; line-height: 12.5px;
    color: var(--text-light);
  }
  .contact .contact__name { color: var(--brand-green); }

  /* Envelope front */
  .envelope-front { left: 581px; top: 37px; width: 598px; height: 257px; }
  .envelope-front .wordmark { left: 18px; top: 18px; font-size: 18px; }
  .envelope-front .sender {
    position: absolute; left: 30px; top: 51px;
    font-size: 7px; line-height: 9.5px; color: var(--text-dark);
  }
  .envelope-front .recipient {
    position: absolute; left: 360px; top: 85px;
    text-align: center; font-size: 12.5px; line-height: 16px; color: var(--text-dark);
  }
  .envelope-front .band--bottom { bottom: 0; height: 50px; }

  /* Envelope back */
  .envelope-back { left: 581px; top: 340px; width: 598px; height: 258px; }
  .envelope-back .band--flap { top: 0; height: 88px; }
  .envelope-back .wordmark {
    left: 0; right: 0; top: 30px; text-align: center; font-size: 18px;
  }
</style>
</head>
<body>

<section class="sheet letterhead" aria-label="Letterhead">
  <svg class="band band--top" viewBox="0 0 525 94" preserveAspectRatio="none" aria-hidden="true">
    <defs>
      <linearGradient id="headShade" x1="0" y1="0" x2="0" y2="1">
        <stop offset="0" stop-color="#6f6c6d"/>
        <stop offset="1" stop-color="#353133"/>
      </linearGradient>
    </defs>
    <rect width="525" height="88" fill="url(#headShade)"/>
    <path d="M0 22 Q 140 6 300 18 Q 420 26 525 12 V88 H0 Z" fill="var(--band)"/>
    <path d="M0 88 Q 260 82 525 86 V90 Q 260 86 0 92 Z" fill="var(--brand-green)"/>
  </svg>
  <div class="wordmark">Panelcraft</div>
  <address class="contact" style="font-style:normal">
    <div class="contact__name">Daniel Marsh</div>
    <div>820 Bodyline Avenue Westbrook 3310</div>
    <div>CA 94512</div>
    <div>T: 00-000-0000</div>
  </address>
  <svg class="band band--bottom" viewBox="0 0 525 60" preserveAspectRatio="none" aria-hidden="true">
    <path d="M0 30 Q 250 18 390 6 Q 460 2 500 16 Q 320 14 0 34 Z" fill="#c9c9c9"/>
    <path d="M0 32 Q 260 20 525 24 V60 H0 Z" fill="var(--band)"/>
  </svg>
</section>

<section class="sheet envelope-front" aria-label="Envelope front">
  <div class="wordmark">Panelcraft</div>
  <address class="sender" style="font-style:normal">
    <div>Daniel Marsh</div>
    <div>820 Bodyline Avenue Westbrook 3310</div>
    <div>CA 94512</div>
    <div>T: 00-000-0000</div>
  </address>
  <div class="recipient">
    <div>Name Customer customer</div>
    <div>Adresss street street</div>
    <div>CA 98087</div>
  </div>
  <svg class="band band--bottom" viewBox="0 0 598 50" preserveAspectRatio="none" aria-hidden="true">
    <path d="M0 22 Q 300 12 420 2 Q 500 -2 560 8 Q 320 8 0 24 Z" fill="#c9c9c9"/>
    <path d="M0 20 Q 300 10 598 16 V50 H0 Z" fill="var(--band)"/>
  </svg>
</section>

<section class="sheet envelope-back" aria-label="Envelope back">
  <svg class="band band--flap" viewBox="0 0 598 88" preserveAspectRatio="none" aria-hidden="true">
    <path d="M0 0 H598 V20 L578 74 Q 573 86 560 86 H38 Q 25 86 20 74 L0 20 Z" fill="var(--band)"/>
  </svg>
  <div class="wordmark">Panelcraft</div>
</section>

</body>
</html>
```